Guitar parts retail packaging

I have 2 boxes I need designed. This will be for my guitar parts. They are going to be thick cardstock type paper box, with a foam insert to secure the items. Matte finish with silver foil printing is sort of where im headed, but Im open to other beautiful design. The boxes will need to have a window on top of the box to show the product inside. Color scheme Im thinking with is Black with red, white and Silver foil printing. Unless you come up with something nicer, im open to that. But my business cards and some stickers are those colors.
2 different size boxes, but they can be the same basic design, modified for 2 different sizes. They will open at the front, and the lid will lift, hinged at the top back edge. (Please see purple box in picture for example for how box will work). Both boxes will have a window on top to showcase product in the box. One of the sides, (2" X 1.25") will be left a solid color, grey or other so I can put a product sticker on that side to designate what type of product is in the box. So you are really just designing the top (With window), front, back, and 1 side. Maybe something clever on the bottom but if thats blank thats fine.
LARGE BOX:
5.25 wide (Left to right)
2” deep (Front to back)
1.25” tall (Top to bottom)
SMALL BOX:
2” Wide (Left to right)
2” Deep (Front to back)
Please see Business card and sticker in picture for color scheme Im thinking. ( I am open to other colors and designs as well)

Target Market(s)

Musicians, Rockers, tattoo junkies, general badasses.

Industry/Entity Type

Guitar industry. Rock & Rollers

Font styles to use
Other font styles liked:
• I use a font called Morpheus for my logo. Also Times New Roman, maybe Copperplate? Or something more creative? Im open as long as it fits.

Colors
EB3D1F
EC4F4E
F09395
F8D3D4
FCEDEE

Requirements
Must have
• My Company name and logo (Harrow Kestrel). Also slogan-
Nice to have
• Please see general aesthetic in sticker and biz card.
Should not have
• No horror themes, keep it cool and classy. (Even though logo is a skull). And please no pictures of guitars on the box. You might add a pic of 1 type of guitar, but the parts inside might not fit that guitar pictured on the box.

```html
<!DOCTYPE html>
<html lang="en">
<head>
<meta charset="utf-8">
<title>Harrow Kestrel — Guitar Parts Box</title>
<link rel="stylesheet" href="https://fonts.googleapis.com/css2?family=Cinzel:wght@400;600&display=swap">
<style>
  :root {
    --stage-grey: #cfcfcf;
    --box-black: #141414;
    --box-black-soft: #232323;
    --crimson-deep: #7d0f10;
    --crimson: #b3140f;
    --crimson-bright: #c81c12;
    --silver: #e6e6e6;
    --window-white: #f2f2f2;
  }
  * { box-sizing: border-box; margin: 0; padding: 0; }
  html, body {
    width: 1200px;
    height: 882px;
    overflow: hidden;
    background: var(--stage-grey);
  }
  .box-artwork {
    position: absolute;
    left: 110px;
    top: 150px;
    width: 980px;
    height: 582px;
    box-shadow: 0 18px 40px rgba(0, 0, 0, 0.22);
  }
  .lid-band {
    position: absolute;
    left: 0;
    top: 0;
    width: 980px;
    height: 132px;
    background: linear-gradient(180deg, var(--box-black-soft), var(--box-black));
    border-bottom: 2px solid #0a0a0a;
  }
  .lid-band .pattern-fill {
    position: absolute;
    inset: 0;
  }
  .lid-band .lid-name {
    position: absolute;
    right: 90px;
    top: 30px;
    font-family: "Cinzel", serif;
    font-weight: 600;
    font-size: 40px;
    letter-spacing: 2px;
    color: var(--silver);
    text-align: right;
  }
  .lid-band .lid-slogan {
    position: absolute;
    right: 150px;
    top: 80px;
    font-family: "Cinzel", serif;
    font-weight: 400;
    font-size: 20px;
    letter-spacing: 3px;
    color: var(--silver);
  }
  .front-face {
    position: absolute;
    left: 0;
    top: 132px;
    width: 980px;
    height: 450px;
  }
  .front-face svg { position: absolute; inset: 0; }
  .brand-lockup {
    position: absolute;
    left: 40px;
    top: 70px;
    width: 560px;
    text-align: center;
    color: var(--silver);
    font-family: "Cinzel", serif;
  }
  .brand-mark {
    display: block;
    width: 46px;
    height: 46px;
    margin: 0 auto 22px;
    border-radius: 50%;
    background: var(--silver);
  }
  .brand-name {
    display: block;
    font-weight: 600;
    font-size: 58px;
    letter-spacing: 2px;
    line-height: 1.1;
  }
  .brand-slogan {
    display: block;
    margin-top: 18px;
    font-weight: 400;
    font-size: 28px;
    letter-spacing: 4px;
  }
</style>
</head>
<body>
  <main class="box-artwork">
    <section class="lid-band">
      <svg class="pattern-fill" width="980" height="132" role="img" aria-label="Dark black-on-black damask pattern across the lid">
        <defs>
          <radialGradient id="lidDamask" cx="50%" cy="50%" r="70%">
            <stop offset="0" stop-color="#262626"/>
            <stop offset="1" stop-color="#121212"/>
          </radialGradient>
        </defs>
        <rect width="980" height="132" fill="url(#lidDamask)"/>
      </svg>
      <div class="lid-name">Harrow Kestrel</div>
      <div class="lid-slogan">Rock &amp; Roll Royalty</div>
    </section>

    <section class="front-face">
      <svg width="980" height="450" viewBox="0 0 980 450">
        <defs>
          <linearGradient id="crimsonPanel" x1="0" y1="0" x2="1" y2="1">
            <stop offset="0" stop-color="var(--crimson-deep)"/>
            <stop offset="0.6" stop-color="var(--crimson)"/>
            <stop offset="1" stop-color="var(--crimson-bright)"/>
          </linearGradient>
          <radialGradient id="blackDamask" cx="75%" cy="50%" r="60%">
            <stop offset="0" stop-color="#242424"/>
            <stop offset="1" stop-color="#111"/>
          </radialGradient>
        </defs>
        <rect class="black-field" width="980" height="450" fill="url(#blackDamask)" role="img" aria-label="Black damask pattern background"/>
        <polygon class="crimson-panel" points="0,0 720,0 560,450 0,450" fill="url(#crimsonPanel)" role="img" aria-label="Crimson panel with faint tonal damask pattern"/>
        <rect class="product-window" x="630" y="150" width="300" height="170" rx="30" fill="var(--window-white)"/>
      </svg>
      <div class="brand-lockup">
        <span class="brand-mark"></span>
        <span class="brand-name">Harrow Kestrel</span>
        <span class="brand-slogan">Rock &amp; Roll Royalty</span>
      </div>
    </section>
  </main>
</body>
</html>
```